Flyer-Design zum Thema Elektrosmog
Zielgruppe
Wir machen Schlafplatzanalysen auf Elektrosmog.
Elektrosmog entsteht zum Beispiel durch die Stromversorgung im Haus oder durch Funkübertragung wie Mobiltelefon, W-LAN, Bluetooth, etc.
Unsere Zielgruppe sind private Kunden. Im Wesentlichen:
- Frauen mittleren Alters,
- junge Mütter,
- Familien.
Aufgabenstellung
Flyer zum Thema Elektrosmog
Der Flyer soll in Praxen von Heilpraktikern ausgelegt werden oder auch als gezielte Wurfsendung für bestimmte Wohngebiete genutzt werden. Im Prinzip eine Visitenkarte mit Infos.
Faltblatt, geschlossenes Endformat DIN A7 (7,4 x 10,5 cm) / 4 Seiten
Hoch oder quer gefaltet möglich
Bitte Vorschläge zu Papier und Druck
Alternativ:
Produktdetails von Druckwerkel
4/4-farbig (beidseitiger Druck)
Material: 400 g Bilderdruck matt
Veredelung beidseitiger Dispersionslack matt
Seite 1:
Logo: Bogen in gold, Rest schwarz
Text: Erholsam schlafen trotz Elektrosmog für Groß und Klein
Seite 2 und 3 (Innen)
Text:
Fühlen Sie oder Ihre Kinder sich am Morgen trotz ausreichender Schlafdauer müde und zerschlagen?
Elektrosmog kann die Ursache sein.
Wir bieten:
• Ermittlung der Belastung an Ihrem Schlafplatz mit professionellen Messgeräten
• Beratung nach dem Prinzip 1. Abschalten, 2. Abstand, 3. Abschirmen
• Strahlungsarmen und damit erholsamen Schlaf

```html
<!DOCTYPE html>
<html lang="de">
<head>
<meta charset="utf-8">
<title>Flyer Elektrosmog – Schlafplatzanalyse</title>
<link rel="stylesheet" href="https://fonts.googleapis.com/css2?family=PT+Sans:ital,wght@0,400;0,700;1,400;1,700&display=swap">
<style>
  :root {
    --navy: #0d1f47;
    --gold: #c99d63;
    --gold-text: #b8864a;
    --arc-gold: #d4a933;
    --backdrop: #b9b9b9;
    --paper: #ffffff;
    --rule: #d8d8d8;
    --photo-light: #f1efee;
    --photo-mid: #e2d6cc;
    --photo-warm: #c9ad98;
  }
  * { margin: 0; padding: 0; box-sizing: border-box; }
  html, body { width: 1200px; height: 2818px; overflow: hidden; background: var(--backdrop); }
  body { font-family: "PT Sans", sans-serif; color: var(--navy); }

  .stage { position: absolute; left: 0; top: 0; width: 1097px; height: 2576px; transform: scale(1.0939); transform-origin: 0 0; }

  .panel { position: absolute; background: var(--paper); overflow: hidden; }
  .panel > svg { position: absolute; left: 0; top: 0; }
  .page { position: absolute; top: 0; width: 367px; height: 523px; overflow: hidden; }

  /* Cover */
  .brand { position: absolute; left: 0; width: 367px; top: 78px; text-align: center; font-weight: 700; font-size: 28px; color: var(--navy); }
  .brand::before { content: ""; display: inline-block; width: 12px; height: 12px; border-radius: 50%; background: var(--navy); margin-right: 8px; vertical-align: middle; position: relative; top: -2px; }
  .cover-title { position: absolute; left: 0; width: 367px; top: 175px; text-align: center; font-style: italic; }
  .cover-title .line { font-size: 23px; line-height: 29px; }
  .cover-title strong { font-weight: 700; }
  .cover-title .rule { width: 200px; height: 1.5px; background: var(--navy); margin: 2px auto 6px; }
  .cover-title .sub { font-size: 16px; font-weight: 700; }

  /* Back */
  .back-contact { position: absolute; left: 76px; top: 288px; font-size: 15px; line-height: 19px; }
  .back-contact .kicker { font-size: 15px; }
  .back-contact .topic { font-size: 20px; font-weight: 700; line-height: 22px; margin-bottom: 9px; }
  .back-contact .name { font-weight: 700; }
  .back-contact .title { font-size: 12.5px; line-height: 16px; }
  .back-contact .address { margin-top: 8px; }
  .back-contact .phone { font-weight: 700; margin-top: 4px; }

  /* Inside */
  .question { position: absolute; left: 36px; top: 368px; width: 300px; font-size: 14.5px; line-height: 19px; color: var(--gold-text); }
  .cause { position: absolute; left: 36px; top: 439px; font-size: 14.5px; }
  .cause strong { font-size: 18px; }
  .offer-head { position: absolute; left: 393px; top: 50px; font-size: 20px; font-weight: 700; color: var(--gold); letter-spacing: .3px; }
  .offer-list { position: absolute; left: 393px; top: 90px; width: 320px; list-style: none; font-size: 15px; line-height: 20px; }
  .offer-list li { padding-left: 12px; text-indent: -11px; margin-bottom: 3px; }
  .offer-list li::before { content: "• "; }
  .steps { position: absolute; left: 396px; top: 163px; width: 320px; display: flex; font-size: 15px; font-weight: 700; }
  .steps span:nth-child(1) { width: 110px; }
  .steps span:nth-child(2) { width: 98px; }
  .closing { position: absolute; left: 413px; top: 440px; color: var(--gold); }
  .closing .lead { font-size: 16px; }
  .closing .claim { font-size: 19.5px; font-weight: 700; font-style: italic; padding-left: 10px; }
</style>
</head>
<body>
<svg width="0" height="0" style="position:absolute">
  <defs>
    <symbol id="sparkle" viewBox="-12 -12 24 24"><path d="M0,-12 Q1.6,-1.6 12,0 Q1.6,1.6 0,12 Q-1.6,1.6 -12,0 Q-1.6,-1.6 0,-12Z"/></symbol>
    <linearGradient id="photoTone" x1="0" y1="0" x2="0.3" y2="1">
      <stop offset="0" stop-color="#f1efee"/>
      <stop offset="0.55" stop-color="#e2d6cc"/>
      <stop offset="1" stop-color="#c9ad98"/>
    </linearGradient>
    <linearGradient id="morningTone" x1="0" y1="0" x2="1" y2="1">
      <stop offset="0" stop-color="#e9e6e4"/>
      <stop offset="0.6" stop-color="#b7aea8"/>
      <stop offset="1" stop-color="#8c8582"/>
    </linearGradient>
  </defs>
</svg>

<main class="stage">

  <!-- Cover single -->
  <section class="panel" style="left:360px;top:120px;width:367px;height:523px;">
    <div class="page cover" style="left:0">
      <svg width="367" height="523" viewBox="0 0 367 523">
        <path d="M0,113 Q183,195 367,118 L367,502 L0,502Z" fill="url(#photoTone)" role="img" aria-label="Foto: Vater und Tochter schlafen entspannt im Bett"/>
        <path d="M0,113 Q183,195 367,118" fill="none" stroke="var(--gold)" stroke-width="4"/>
        <rect x="0" y="502" width="367" height="21" fill="var(--gold)"/>
        <use href="#sparkle" x="318" y="453" width="24" height="24" fill="var(--navy)"/>
        <use href="#sparkle" x="289" y="476" width="32" height="32" fill="var(--navy)"/>
      </svg>
      <div class="brand">wellruhig</div>
      <div class="cover-title">
        <div class="line">Erholsam schlafen</div>
        <div class="line">trotz <strong>ELEKTROSMOG</strong></div>
        <div class="rule"></div>
        <div class="sub">für Groß und Klein</div>
      </div>
    </div>
  </section>

  <!-- Inside spread -->
  <section class="panel inside" style="left:182px;top:717px;width:737px;height:523px;">
    <svg width="737" height="523" viewBox="0 0 737 523">
      <circle cx="165" cy="128" r="200" fill="url(#morningTone)" role="img" aria-label="Foto: müder Mann reibt sich morgens im Bett die Augen"/>
      <circle cx="165" cy="128" r="200" fill="none" stroke="var(--gold)" stroke-width="3"/>
      <use href="#sparkle" x="33" y="272" width="46" height="46" fill="var(--navy)"/>
      <use href="#sparkle" x="22" y="327" width="26" height="26" fill="var(--navy)"/>
      <line x1="369" y1="40" x2="369" y2="475" stroke="var(--rule)" stroke-width="1.5"/>
      <rect x="393" y="200" width="320" height="148" rx="6" fill="#f3efe9" role="img" aria-label="Illustrationen: Schalter, Handy und Steckdose mit Abstand zum Bett, Abschirmung über dem Kinderbett"/>
      <path d="M305,523 Q500,320 737,395" fill="none" stroke="var(--gold)" stroke-width="4"/>
      <path d="M318,523 Q505,335 737,405 L737,523Z" fill="var(--navy)"/>
      <use href="#sparkle" x="644" y="392" width="34" height="34" fill="var(--gold)"/>
      <use href="#sparkle" x="687" y="431" width="26" height="26" fill="var(--gold)"/>
    </svg>
    <p class="question">Fühlen Sie oder Ihre Kinder sich am Morgen trotz ausreichender Schlafdauer müde und zerschlagen?</p>
    <p class="cause"><strong>ELEKTROSMOG</strong> kann die Ursache sein.</p>
    <h2 class="offer-head">WIR BIETEN IHNEN:</h2>
    <ul class="offer-list">
      <li><strong>Ermittlung</strong> der Belastung an Ihrem Schlaf&shy;platz mit professionellen Messgeräten</li>
      <li><strong>Beratung</strong> nach dem Prinzip:</li>
    </ul>
    <div class="steps"><span>1. Abschalten</span><span>2. Abstand</span><span>3. Abschirmen</span></div>
    <div class="closing">
      <div class="lead">• Strahlungsarmen</div>
      <div class="claim">und damit erholsamen Schlaf</div>
    </div>
  </section>

  <!-- Back single -->
  <section class="panel" style="left:361px;top:1310px;width:367px;height:523px;">
    <div class="page back" style="left:0">
      <svg width="367" height="523" viewBox="0 0 367 523">
        <path d="M0,0 H367 V100 Q150,85 0,180Z" fill="var(--navy)"/>
        <path d="M0,190 Q150,95 367,110" fill="none" stroke="var(--gold)" stroke-width="4"/>
        <use href="#sparkle" x="38" y="39" width="34" height="34" fill="var(--gold)"/>
        <use href="#sparkle" x="67" y="78" width="26" height="26" fill="var(--gold)"/>
        <rect x="0" y="501" width="367" height="22" fill="var(--gold)"/>
      </svg>
      <div class="back-contact">
        <div class="kicker">Schlafplatzanalyse</div>
        <div class="topic">ELEKTROSMOG</div>
        <div class="name">Hanna Brenneis</div>
        <div class="title">Dipl.-Ing. (FH) der Elektrotechnik</div>
        <div class="name">Lukas Brenneis</div>
        <div class="address">Lindenweg 17<br>64380 Feldbach</div>
        <div class="phone">T 06123. 456 780</div>
      </div>
    </div>
  </section>

  <!-- Outside spread -->
  <section class="panel" style="left:175px;top:1935px;width:737px;height:523px;">
    <div class="page back" style="left:0">
      <svg width="367" height="523" viewBox="0 0 367 523">
        <path d="M0,0 H367 V100 Q150,85 0,180Z" fill="var(--navy)"/>
        <path d="M0,190 Q150,95 367,110" fill="none" stroke="var(--gold)" stroke-width="4"/>
        <use href="#sparkle" x="38" y="39" width="34" height="34" fill="var(--gold)"/>
        <use href="#sparkle" x="67" y="78" width="26" height="26" fill="var(--gold)"/>
        <rect x="0" y="501" width="367" height="22" fill="var(--gold)"/>
      </svg>
      <div class="back-contact">
        <div class="kicker">Schlafplatzanalyse</div>
        <div class="topic">ELEKTROSMOG</div>
        <div class="name">Hanna Brenneis</div>
        <div class="title">Dipl.-Ing. (FH) der Elektrotechnik</div>
        <div class="name">Lukas Brenneis</div>
        <div class="address">Lindenweg 17<br>64380 Feldbach</div>
        <div class="phone">T 06123. 456 780</div>
      </div>
    </div>
    <div class="page cover" style="left:368px">
      <svg width="367" height="523" viewBox="0 0 367 523">
        <path d="M0,113 Q183,195 367,118 L367,502 L0,502Z" fill="url(#photoTone)" role="img" aria-label="Foto: Vater und Tochter schlafen entspannt im Bett"/>
        <path d="M0,113 Q183,195 367,118" fill="none" stroke="var(--gold)" stroke-width="4"/>
        <rect x="0" y="502" width="367" height="21" fill="var(--gold)"/>
        <use href="#sparkle" x="318" y="453" width="24" height="24" fill="var(--navy)"/>
        <use href="#sparkle" x="289" y="476" width="32" height="32" fill="var(--navy)"/>
      </svg>
      <div class="brand">wellruhig</div>
      <div class="cover-title">
        <div class="line">Erholsam schlafen</div>
        <div class="line">trotz <strong>ELEKTROSMOG</strong></div>
        <div class="rule"></div>
        <div class="sub">für Groß und Klein</div>
      </div>
    </div>
  </section>

</main>
</body>
</html>
```